DOUBLE SIDED BROCHURE NEEDED TO PROMOTE DOCTOR

I need a double sided DL size (99mm x 210mm) brochure, promoting a doctor seeing patients in a new area.

I want something professional. I have included the relevant information. I would also like the Dr's picture somwhere in the brochure, with a professional background. I wish to print these tomorrow, so i will pick a winner within 14 hours of posting this ad.

I have included an example of a brochures design that I recently saw, and its definietly a good starting point.

Medical

```html
<!DOCTYPE html>
<html lang="en">
<head>
<meta charset="utf-8">
<title>Dr. Samir Haddad – Referral Brochure</title>
<link href="https://fonts.googleapis.com/css2?family=Nunito:wght@300;400;700;800&display=swap" rel="stylesheet">
<style>
:root{
  --stage:#eceff2;
  --brand:#29abe2;
  --brand-deep:#1a96d6;
  --band:#0ba7e6;
  --band-cross:#33bdf0;
  --ink:#2f3337;
  --ink-soft:#3d4247;
  --panel-top:#f7fbfe;
  --panel-bottom:#dcedfa;
  --cross:#a9d1f0;
  --cross-light:#c9e2f6;
  --frame:#a3d8f4;
}
*{margin:0;padding:0;box-sizing:border-box}
html,body{width:1200px;height:1053px;overflow:hidden;background:var(--stage)}
body{font-family:"Nunito",sans-serif;color:var(--ink)}
.stage{position:relative;width:1200px;height:1053px}
.panel{position:absolute;top:30px;width:468px;height:993px;overflow:hidden;
  background:linear-gradient(180deg,var(--panel-top) 0%,#eef6fd 55%,var(--panel-bottom) 100%);
  box-shadow:0 4px 14px rgba(0,0,0,.12)}
.panel--front{left:102px}
.panel--back{left:630px;background:linear-gradient(180deg,#dff0fc 0%,#eef7fe 40%,#f6fbff 80%)}
.abs{position:absolute}

/* front */
.hero{left:0;top:0;width:468px;height:350px}
.greeting-icon{left:36px;top:382px;width:62px;height:70px}
.greeting{left:112px;top:384px;font-weight:800;font-size:33px;line-height:33px;color:var(--brand);letter-spacing:.5px}
.body-copy{left:36px;width:380px;font-size:16.5px;line-height:27.5px;font-weight:400;color:var(--ink-soft)}
.body-copy strong{font-weight:800;color:var(--ink)}
.copy-1{top:463px}
.copy-2{top:574px}
.clinic-name{font-weight:800;font-size:26px;color:var(--brand)}
.clinic-address{font-size:17px;line-height:23px;color:var(--ink-soft)}
.front-clinic{left:36px;top:726px}
.front-address{left:36px;top:758px}
.phone-box{width:206px;height:47px;border:2px solid var(--brand);border-radius:8px;
  display:flex;align-items:center;gap:6px;padding-left:6px;font-weight:800;font-size:25px;color:var(--brand)}
.front-phone{left:32px;top:832px;background:#fff}
.fax-label{left:31px;top:906px;font-size:15px;color:var(--ink)}
.fax-line{left:32px;top:934px;display:flex;align-items:center;gap:8px;font-weight:800;font-size:23px;color:var(--brand)}
.crosses{right:0;bottom:0;width:220px;height:200px}

/* back */
.back-hexes{left:0;top:0;width:468px;height:90px}
.portrait{left:28px;top:36px;width:230px;height:258px}
.doctor-name{left:266px;top:118px;font-weight:800;font-size:42px;line-height:45px;color:var(--ink)}
.intro{left:36px;top:312px;width:410px;font-size:17px;line-height:28px;color:var(--ink-soft)}
.item{left:36px;font-size:17.5px;display:flex;align-items:center;gap:10px;color:var(--ink)}
.item svg{flex:none}
.item-sub{left:62px;font-size:14.5px;color:var(--ink-soft)}
.section-lead{left:36px;font-size:17px;color:var(--ink-soft)}
.band{left:0;top:784px;width:468px;height:209px;background:var(--band)}
.band .clinic-name{color:#fff}
.band .clinic-address{color:#fff}
.back-clinic{left:39px;top:22px}
.back-address{left:39px;top:53px}
.back-phone{left:35px;top:124px;border-color:#fff;color:#fff}
.band-crosses{right:0;bottom:0;width:200px;height:190px}
</style>
</head>
<body>
<main class="stage">

  <!-- Front side -->
  <section class="panel panel--front">
    <svg class="abs hero" viewBox="0 0 468 350" role="img" aria-label="Photo of the surgeon standing in front of a modern hospital building under a blue sky">
      <defs>
        <linearGradient id="heroPhoto" x1="0" y1="0" x2="0" y2="1">
          <stop offset="0" stop-color="#5d8fcf"/>
          <stop offset=".45" stop-color="#b9cfe4"/>
          <stop offset="1" stop-color="#6b7a86"/>
        </linearGradient>
      </defs>
      <polygon points="0,0 468,0 468,185 400,345 78,345 0,210" fill="var(--frame)"/>
      <polygon points="0,0 468,0 468,161 403,330 83,330 0,179" fill="url(#heroPhoto)"/>
      <polyline points="0,150 92,318 400,318 468,150" fill="none" stroke="var(--brand-deep)" stroke-width="6" opacity=".7"/>
    </svg>

    <svg class="abs greeting-icon" viewBox="0 0 62 70" aria-hidden="true">
      <polygon points="31,0 62,17.5 62,52.5 31,70 0,52.5 0,17.5" fill="var(--brand)"/>
      <path d="M22 20v12a9 9 0 0 0 18 0V20" fill="none" stroke="#fff" stroke-width="3" stroke-linecap="round"/>
      <path d="M31 41v6a8 8 0 0 0 16 0v-6" fill="none" stroke="#fff" stroke-width="3" stroke-linecap="round"/>
      <circle cx="47" cy="38" r="3.5" fill="none" stroke="#fff" stroke-width="2.5"/>
    </svg>
    <h1 class="abs greeting">DEAR<br>DOCTORS,</h1>

    <p class="abs body-copy copy-1">We are pleased to announce that <strong>Dr. Samir Haddad</strong> is now consulting in Seabrook, seeing public and private patients.</p>
    <p class="abs body-copy copy-2">Guaranteed appointment within two weeks, with patients having the option of surgery at Harbourside Health Campus, Westbrook Hospital or St. Clare Riverside.</p>

    <h2 class="abs clinic-name front-clinic">Seabrook Clinic</h2>
    <p class="abs clinic-address front-address">42 Harbour View Road,<br>Seabrook WA 6299</p>

    <div class="abs phone-box front-phone">
      <svg width="22" height="36" viewBox="0 0 22 36" aria-hidden="true"><path d="M8 2h7v9H10q-3 7 0 14h5v9H8Q0 26 0 18T8 2z" fill="none" stroke="var(--brand)" stroke-width="3"/></svg>
      <span>1300 555 014</span>
    </div>

    <p class="abs fax-label">Please send all referrals by fax to</p>
    <div class="abs fax-line">
      <svg width="32" height="28" viewBox="0 0 32 28" aria-hidden="true"><rect x="8" y="0" width="16" height="8" fill="var(--brand)"/><rect x="0" y="8" width="32" height="14" rx="3" fill="var(--brand)"/><rect x="7" y="16" width="18" height="12" fill="#fff" stroke="var(--brand)" stroke-width="2.5"/></svg>
      <span>(08) 5550 2841</span>
    </div>

    <svg class="abs crosses" viewBox="0 0 220 200" aria-hidden="true">
      <path d="M70 90h52V60h52v30h46v62h-46v48h-52v-48H70z" fill="var(--cross)"/>
      <path d="M0 50h28V28h34v22h28v34H62v28H28V84H0z" fill="var(--cross)" opacity=".8"/>
      <path d="M64 8h14V0h22v8h14v20h-14v14H78V28H64z" fill="var(--cross-light)"/>
    </svg>
  </section>

  <!-- Back side -->
  <section class="panel panel--back">
    <svg class="abs back-hexes" viewBox="0 0 468 90" aria-hidden="true">
      <polygon points="0,0 125,0 125,30 70,70 0,70" fill="#bfe3f8" opacity=".7"/>
      <polygon points="155,0 370,0 370,30 300,75 225,75 155,30" fill="#bfe3f8" opacity=".7"/>
    </svg>

    <svg class="abs portrait" viewBox="0 0 230 258" role="img" aria-label="Head-and-shoulders photo of Dr. Samir Haddad">
      <defs>
        <linearGradient id="portraitPhoto" x1="0" y1="0" x2="0" y2="1">
          <stop offset="0" stop-color="#a9c7e8"/>
          <stop offset=".55" stop-color="#8c8f94"/>
          <stop offset="1" stop-color="#2f3a4a"/>
        </linearGradient>
      </defs>
      <polygon points="115,4 226,66 226,192 115,254 4,192 4,66" fill="url(#portraitPhoto)" stroke="var(--brand-deep)" stroke-width="7"/>
    </svg>

    <h1 class="abs doctor-name">Dr. Samir<br>Haddad</h1>

    <p class="abs intro">Dr. Haddad is a highly trained specialised surgeon, in all areas of Endocrine, Breast and General Surgery. Including;</p>

    <div class="abs item" style="top:405px"><svg width="16" height="18" viewBox="0 0 16 18"><polygon points="8,0 16,4.5 16,13.5 8,18 0,13.5 0,4.5" fill="var(--brand)"/></svg>Thyroid Surgery</div>
    <div class="abs item" style="top:435px"><svg width="16" height="18" viewBox="0 0 16 18"><polygon points="8,0 16,4.5 16,13.5 8,18 0,13.5 0,4.5" fill="var(--brand)"/></svg>Parathyroid surgery</div>
    <div class="abs item-sub" style="top:461px">(including minimally invasive parathyroidectomy)</div>
    <div class="abs item" style="top:486px"><svg width="16" height="18" viewBox="0 0 16 18"><polygon points="8,0 16,4.5 16,13.5 8,18 0,13.5 0,4.5" fill="var(--brand)"/></svg>Breast Cancer</div>
    <div class="abs item-sub" style="top:512px">Benign breast lesions</div>

    <p class="abs section-lead" style="top:558px">All areas of general surgery, such as;</p>

    <div class="abs item" style="top:598px"><svg width="16" height="18" viewBox="0 0 16 18"><polygon points="8,0 16,4.5 16,13.5 8,18 0,13.5 0,4.5" fill="var(--brand)"/></svg>Gallbladder surgery</div>
    <div class="abs item" style="top:629px"><svg width="16" height="18" viewBox="0 0 16 18"><polygon points="8,0 16,4.5 16,13.5 8,18 0,13.5 0,4.5" fill="var(--brand)"/></svg>Hernia surgery</div>
    <div class="abs item" style="top:660px"><svg width="16" height="18" viewBox="0 0 16 18"><polygon points="8,0 16,4.5 16,13.5 8,18 0,13.5 0,4.5" fill="var(--brand)"/></svg>Haemorrhoids</div>
    <div class="abs item" style="top:691px"><svg width="16" height="18" viewBox="0 0 16 18"><polygon points="8,0 16,4.5 16,13.5 8,18 0,13.5 0,4.5" fill="var(--brand)"/></svg>Carpal Tunnel</div>
    <div class="abs item" style="top:722px"><svg width="16" height="18" viewBox="0 0 16 18"><polygon points="8,0 16,4.5 16,13.5 8,18 0,13.5 0,4.5" fill="var(--brand)"/></svg>Vasectomy etc etc…</div>

    <div class="abs band">
      <svg class="abs band-crosses" viewBox="0 0 200 190" aria-hidden="true">
        <path d="M56 90h46V62h52v28h46v62h-46v38h-52v-38H56z" fill="var(--band-cross)"/>
        <path d="M0 44h20V24h32v20h20v32H52v22H20V76H0z" fill="var(--band-cross)" opacity=".8"/>
        <path d="M50 8h12V0h20v8h12v18H82v12H62V26H50z" fill="var(--band-cross)" opacity=".8"/>
      </svg>
      <h2 class="abs clinic-name back-clinic">Seabrook Clinic</h2>
      <p class="abs clinic-address back-address">42 Harbour View Road,<br>Seabrook WA 6299</p>
      <div class="abs phone-box back-phone">
        <svg width="22" height="36" viewBox="0 0 22 36" aria-hidden="true"><path d="M8 2h7v9H10q-3 7 0 14h5v9H8Q0 26 0 18T8 2z" fill="none" stroke="#fff" stroke-width="3"/></svg>
        <span>1300 555 014</span>
      </div>
    </div>
  </section>

</main>
</body>
</html>
```